Internet Service Provider Corporate Brochure

We require 2 brochures designed, one including price and one excluding price. We are looking for a professional and fresh design that ties in with our brand colours, but that isn't necessarily limited to them. All copy and information is contained in our attached file, and once we have appointed a designer we will include the file containing the costs as well.
Updates

Project Deadline Extended
Reason: I feel this design will require more time to complete without stress...

Target Market(s)

Corporate Companies. Internet Users. Small to medium enterprises. CEOs. CTOs. IT Managers

Industry/Entity Type

Internet Service Provider

Font styles to use
Sans Serif

Requirements
Must have
• Clean look and feel. Hyperlinks to our website. Focus on design so copy isn't too "in your face" and wordy. Must use our corporate colours but have other complementary colour too.
Nice to have
• Organic flow from one product and service to the next. Something that appears to have clean texture rather than flat design.
Should not have
• excessive white or unused space. Rounded fonts and cursive fonts. no pink. No text boxes within other boxes.

```html
<!DOCTYPE html>
<html lang="en">
<head>
<meta charset="utf-8">
<title>Prismnet – Pay Per Account</title>
<link rel="stylesheet" href="https://fonts.googleapis.com/css2?family=Open+Sans:wght@400;600;700&display=swap">
<style>
  :root{
    --backdrop:#2e2e2e;
    --paper:#ffffff;
    --slate:#6a6a6a;
    --ink:#3a3a3a;
    --light:#eeeeee;
    --rule:#bdbdbd;
    --lime:#8cc63f;
    --lime-dark:#7ab32f;
    --black:#111111;
  }
  *{box-sizing:border-box;margin:0;padding:0}
  html,body{width:849px;height:1200px;overflow:hidden}
  body{background:var(--backdrop);font-family:"Open Sans",Arial,sans-serif;position:relative}
  .page{position:absolute;left:62px;top:57px;width:725px;height:1086px;background:var(--slate)}
  .intro{background:var(--paper);height:305px;padding:92px 51px 0 51px}
  .brand{display:flex;align-items:center;gap:12px;font-size:44px;font-weight:700;color:var(--lime);letter-spacing:-1px;line-height:1}
  .brand-dot{width:22px;height:22px;border-radius:50%;background:var(--lime)}
  .intro-text{margin-top:36px;font-size:11.5px;line-height:1.55;color:var(--ink)}
  .product{padding:40px 51px 0 51px;color:var(--light)}
  .product-title{font-size:22px;font-weight:700;color:#fff;padding-bottom:8px;border-bottom:2px solid #fff;margin-right:-51px}
  .features{display:grid;grid-template-columns:88px 1fr;margin-top:24px;font-size:11px}
  .features-label{font-weight:700;color:#fff;line-height:1.3}
  .features ul{list-style:none}
  .features li{padding:4px 0 8px;border-bottom:1px solid var(--rule);margin-bottom:6px}
  .body-text{font-size:11.5px;line-height:1.55;margin-top:18px}
  .pricing-label{margin-top:150px;font-size:12px;font-weight:700;color:#fff}
  .pricing{margin-top:10px;width:100%;border-collapse:collapse;font-size:11px}
  .pricing th{background:var(--black);color:#fff;text-align:left;font-weight:700;padding:8px 8px;border:2px solid #fff;line-height:1.2}
  .pricing td{height:30px;border-top:2px solid var(--slate);background:var(--lime)}
  .pricing tbody tr:nth-child(even) td{background:var(--lime-dark)}
  .col-spend{width:56%}
  .col-applied{width:22%}
</style>
</head>
<body>
<main class="page">
  <section class="intro">
    <div class="brand"><span class="brand-dot"></span>prismnet</div>
    <p class="intro-text">Prismnet offers the most flexible reseller options in South Africa, catering for every reseller requirement one can hope for. Not only do we provide you with the ability to on-sell standard Prismnet accounts at bulk discounted rates, but we provide you with the flexibility to purchase fully whitelabelled solutions in bulk, such as bulk gigs, pay per GB, and the outright purchase of capacity on our network.</p>
  </section>
  <section class="product">
    <h2 class="product-title">Pay Per Account (PPA)</h2>
    <div class="features">
      <div class="features-label">Product<br>features:</div>
      <ul>
        <li>No need for complex API implementation</li>
        <li>Can be up and running within 24 hours</li>
        <li>Bulk discounts applied on a tiered basis – the more you sell, the more you save</li>
      </ul>
    </div>
    <p class="body-text">This product is ideal for small businesses looking to expand their product offerings without the hassle of complex API integrations. It's also ideally suited to IT technical companies that wish to provide a value added service to ensure that their clients' business data connections remain stable at all times.</p>
    <p class="body-text">This product is not available as a whitelabelled solution and is only provisioned on standard Prismnet realms. Should you wish to wholesale our standard products, normal retail rates apply without discounts. Products available for resellers are all business accounts and capped accounts. Home products are not available for resale on PPA.</p>
    <p class="pricing-label">Pricing:</p>
    <table class="pricing">
      <thead>
        <tr><th class="col-spend">Monthly Data Spend</th><th class="col-applied">Discount<br>Applied</th><th>Discount<br>term</th></tr>
      </thead>
      <tbody>
        <tr><td></td><td></td><td></td></tr>
        <tr><td></td><td></td><td></td></tr>
        <tr><td></td><td></td><td></td></tr>
        <tr><td></td><td></td><td></td></tr>
        <tr><td></td><td></td><td></td></tr>
      </tbody>
    </table>
  </section>
</main>
</body>
</html>
```